Business Cards for Law Office of Denise R. Harlow

I need a business card for my new estate planning law firm. I have attached my logo. I would like a design that is professional but not too formal or stuffy.

Target Market(s)

Professionals (lawyers, doctors, businesswomen) between the age of 30 and 50 who are tech-savvy and educated.

Industry/Entity Type

Lawyer

Contact Information for Business Card

Denise R. Harlow

528 E. 19th Street
7th Floor
New York, NY 10583

Phone: (855) 602-7318
Direct: (917) 463-5071
Email: Denise@DeniseRHarlowLegal.test
www.DeniseRHarlowLegal.test

Font styles to use
Other font styles liked:
• Corbel

Requirements
Must have
• On the front:
• Denise R. Harlow, Esq.
• Owner & Founder
• 528 E. 19th Street
• 7th Floor
• New York, NY 10583
• Phone: (855) 602-7318
• Direct: (917) 463-5071
• Email: denise@deniserharlowlegal.test
• www.deniserharlowlegal.test
• On the back:
• LOGO
Nice to have
• I want it to be professional but not too formal or stuffy. Please choose colors that go with my logo.
Should not have
• I don't want TOO MUCH color. Some color is good, but not too much.

```html
<!DOCTYPE html>
<html lang="en">
<head>
<meta charset="utf-8">
<title>Business Cards – Law Office of Denise R. Harlow</title>
<link rel="stylesheet" href="https://fonts.googleapis.com/css2?family=Source+Sans+3:wght@400;600&display=swap">
<style>
  :root {
    --bg: #2b2b2d;
    --paper: #ffffff;
    --purple: #7a2a7e;
    --orange: #f37621;
    --ink-light: #ffffff;
  }
  * { box-sizing: border-box; margin: 0; padding: 0; }
  html, body { width: 1200px; height: 880px; overflow: hidden; }
  body {
    background: var(--bg);
    font-family: "Source Sans 3", "Corbel", sans-serif;
    position: relative;
  }
  .card {
    position: absolute;
    left: 250px;
    width: 700px;
    height: 400px;
    background: var(--paper);
    overflow: hidden;
    box-shadow: 0 10px 24px rgba(0,0,0,.45);
  }
  .card--back { top: 30px; }
  .card--front { top: 450px; }

  .firm-name {
    position: absolute;
    left: 0; right: 0;
    text-align: center;
    color: var(--purple);
    font-weight: 600;
    text-transform: uppercase;
    letter-spacing: .08em;
    line-height: 1;
  }
  .card--back .firm-name { top: 182px; font-size: 34px; }
  .card--front .firm-name { top: 62px; font-size: 32px; }

  .band { position: absolute; bottom: 28px; }
  .band--address {
    left: 0; width: 372px; height: 124px;
    background: var(--orange);
    padding: 14px 34px 0 20px;
    text-align: right;
    color: var(--ink-light);
    font-size: 17px;
    line-height: 1.25;
  }
  .band--contact {
    left: 372px; right: 0; height: 210px;
    background: var(--purple);
    padding: 46px 20px 0 38px;
    color: var(--ink-light);
    font-size: 16.5px;
  }
  .person-name {
    color: var(--purple);
    font-weight: 600;
    font-size: 22px;
    letter-spacing: .04em;
    text-transform: uppercase;
    margin-bottom: 4px;
  }
  .contact-list { list-style: none; }
  .contact-item {
    display: flex;
    align-items: center;
    gap: 12px;
    height: 30px;
  }
  .contact-icon {
    width: 22px; height: 22px;
    background: var(--orange);
    flex: none;
    display: flex; align-items: center; justify-content: center;
  }
  .contact-icon svg { width: 16px; height: 16px; }
</style>
</head>
<body>

  <section class="card card--back" aria-label="Card back">
    <p class="firm-name">Law Office of Denise R. Harlow</p>
  </section>

  <section class="card card--front" aria-label="Card front">
    <p class="firm-name">Law Office of Denise R. Harlow</p>

    <div class="band band--address">
      <p class="person-name">Denise R. Harlow</p>
      <p>528 E. 19th Street</p>
      <p>7th Floor</p>
      <p>New York, NY 10583</p>
    </div>

    <div class="band band--contact">
      <ul class="contact-list">
        <li class="contact-item">
          <span class="contact-icon"><svg viewBox="0 0 16 16" fill="#fff"><path d="M2 6c0-2 2-3 6-3s6 1 6 3v1h-3V5.5H5V7H2z"/><rect x="3" y="8" width="10" height="5" rx="1"/></svg></span>
          <span>(855) 602-7318</span>
        </li>
        <li class="contact-item">
          <span class="contact-icon"><svg viewBox="0 0 16 16" fill="#fff"><rect x="4.5" y="1.5" width="7" height="13" rx="1.2"/><rect x="5.8" y="3" width="4.4" height="8" fill="#f37621"/></svg></span>
          <span>(917) 463-5071</span>
        </li>
        <li class="contact-item">
          <span class="contact-icon"><svg viewBox="0 0 16 16"><rect x="1.5" y="3.5" width="13" height="9" fill="#fff"/><path d="M1.5 3.5 8 9l6.5-5.5" fill="none" stroke="#f37621" stroke-width="1.3"/></svg></span>
          <span>Denise@DeniseRHarlowLegal.test</span>
        </li>
        <li class="contact-item">
          <span class="contact-icon"><svg viewBox="0 0 16 16" fill="none" stroke="#fff" stroke-width="1.2"><circle cx="8" cy="8" r="6"/><ellipse cx="8" cy="8" rx="2.6" ry="6"/><path d="M2 8h12M3 5h10M3 11h10"/></svg></span>
          <span>www.DeniseRHarlowLegal.test</span>
        </li>
      </ul>
    </div>
  </section>

</body>
</html>
```